International Life Insurer Needs a Web Design

What We Do: We are a boutique financial services firm specializing in solutions that financial services professionals can integrate into comprehensive wealth preservation strategies for their clients. Strategies we provide may run the spectrum from simple life insurance products to complex cases with very sophisticated and intricate solutions.

Industry Type: Financial & Insurance

Top Things to Communicate Through Our Web Design:
#1 Ultra High Net Worth
#2 INTERNATIONAL
#3 Private Banking
#4 Expertise
________________________________________
Our Target Audience:
Financial institutions/private banks who have high net worth/ultra high net worth international clients looking for unparalleled expertise in wealth preservation, taxation, and business insurance. The audience is the financial service professional, not the end client of the financial services. We will direct the professional to the site.
We Like These Designs. (fonts, colors, style):
Simple font, clean, modern, contemporary, blue colors
NOT stodgy, old, gothic, etc.

Secondarily, we’d like to also create a small tri-fold brochure incorporating the web elements (design, text), so the ability to transfer the design to print might be a plus.
Updates

Target Market(s)

Financial services professionals catering to their ultra high net worth clients

Industry/Entity Type

Life Insurance

Requirements
Must have
• Our logo (see uploaded file)
Nice to have
• the existing website includes some text that could be reviewed for ideas and incorporated into the design: http://harborlinecoveragepartners.example/

```html
<!DOCTYPE html>
<html lang="en">
<head>
<meta charset="utf-8">
<title>Harborline Coverage Partners</title>
<link rel="stylesheet" href="https://fonts.googleapis.com/css2?family=Arimo:wght@400;700&family=Source+Sans+3:wght@400;600&display=swap">
<style>
:root{
  --page:#f4f3f4;
  --navy:#22548f;
  --sky:#5bcbee;
  --brand-blue:#1a82e8;
  --ink:#222;
  --muted:#555;
  --rule:#d9d9d9;
  --white:#fff;
}
*{box-sizing:border-box;margin:0;padding:0}
html,body{width:1016px;height:1200px;overflow:hidden}
body{position:relative;background:var(--page);font-family:"Source Sans 3",Arial,sans-serif;color:var(--ink)}
.abs{position:absolute}

/* header */
.brand{left:30px;top:14px;display:flex;align-items:center;gap:10px;text-decoration:none}
.brand-square{width:63px;height:63px;background:var(--navy);flex:none}
.brand-name{font-weight:400;font-size:25px;line-height:24px;color:var(--navy);width:190px}
.main-nav{right:0;top:0;height:73px;display:flex;border-top:1px solid var(--sky)}
.main-nav a{display:flex;align-items:center;padding:0 20px;font-family:Arimo,Arial,sans-serif;font-size:14.5px;color:var(--ink);text-decoration:none;border-left:1px solid var(--rule);white-space:nowrap}
.main-nav a.current{background:var(--sky);border-left:none;width:71px;justify-content:center;padding:0}

/* hero */
.hero{left:0;top:78px}
.slider-dots{left:495px;top:434px;display:flex;gap:1px}
.slider-dots span{width:21px;height:21px;border-radius:50%;background:linear-gradient(#f4f4f4,#c8c8c8);border:1px solid #999}
.slider-dots span.active{background:linear-gradient(#bfeefc,#5bcbee)}

/* service cards */
.service-card{left:29px;width:232px;height:218px;color:var(--white)}
.service-card .photo{position:absolute;inset:0}
.service-card h2{position:absolute;left:12px;top:6px;font-size:30px;font-weight:600;color:var(--white);white-space:nowrap}
.service-card p{position:absolute;left:16px;top:62px;width:206px;font-size:11.5px;line-height:18.5px;color:#111;text-align:justify}
.service-card .more{position:absolute;right:16px;bottom:14px;font-size:15.5px;color:#111}
.service-card .more::before{content:"»";margin-right:6px}
.card-banking .photo{background:linear-gradient(160deg,#b59a85 0%,#e8e6e8 45%,#9eb4c4 100%)}
.card-estate .photo{background:linear-gradient(160deg,#7f93a9 0%,#cdd3da 45%,#6f7e8e 100%)}
.card-life .photo{background:linear-gradient(180deg,#2a5b9e 0%,#7ca8d8 55%,#d8e6f2 100%)}

/* about */
.about-title{left:289px;top:466px;font-size:33px;font-weight:600;color:var(--brand-blue)}
.about-photo{left:288px;top:528px;width:191px;height:176px;border:3px solid #a9a9a9;background:linear-gradient(140deg,#3a2516 0%,#c89a74 50%,#6b4a2f 100%)}
.about-copy{font-size:12px;line-height:27px;color:var(--ink);text-align:justify}
.about-copy.lead{left:502px;top:519px;width:482px}
.about-copy.rest{left:289px;top:715px;width:695px}
.read-more{font-size:16px;color:var(--brand-blue);text-decoration:none}
.read-more::before{content:"»";margin-right:6px;font-size:18px}

/* login */
.login{left:288px;top:840px;width:266px;height:281px;background:var(--navy);padding:12px 13px}
.login-inner{position:relative;width:100%;height:100%;background:#ececec;padding:12px 14px}
.login h3{font-size:25px;font-weight:400;color:var(--brand-blue);line-height:30px}
.login .intro{font-family:Arimo,Arial,sans-serif;font-size:12.5px;line-height:18px;color:#333;margin-top:6px}
.login .register{display:inline-block;margin-top:5px;font-family:Arimo,Arial,sans-serif;font-size:12.5px;color:var(--brand-blue);text-decoration:underline}
.field{display:flex;align-items:center;justify-content:space-between;margin-top:12px;font-family:Arimo,Arial,sans-serif;font-size:12.5px;color:#333;white-space:nowrap}
.field input{width:140px;height:22px;border:1px solid #aaa;background:var(--white)}
.forgot{display:block;text-align:right;font-family:Arimo,Arial,sans-serif;font-size:9.5px;color:var(--brand-blue);margin-top:4px}
.login button{position:absolute;right:10px;bottom:10px;width:66px;height:21px;border:none;border-radius:4px;background:var(--brand-blue);color:var(--white);font-family:Arimo,Arial,sans-serif;font-size:13.5px}

/* advantages */
.advantages-title{left:577px;top:848px;font-family:Arimo,Arial,sans-serif;font-weight:400;font-size:24.5px;color:var(--brand-blue)}
.advantage-list{top:888px;list-style:none}
.advantage-list li{height:21.8px;font-family:Arimo,Arial,sans-serif;font-size:13px;color:#444;text-decoration:underline;white-space:nowrap}
.advantage-list li::before{content:"»";display:inline-block;width:19px;text-decoration:none;color:#333}

/* footer */
.site-footer{left:0;top:1141px;width:1016px;height:59px;background:var(--navy);color:var(--white);font-family:Arimo,Arial,sans-serif;font-size:12.5px}
.site-footer .copy{position:absolute;left:30px;top:23px}
.follow{position:absolute;right:24px;top:11px;display:flex;align-items:center;gap:4px}
.follow .label{margin-right:6px}
.follow a{display:flex;align-items:center;justify-content:center;width:31px;height:31px;border-radius:7px;background:var(--white);border:2px solid #444}
</style>
</head>
<body>

<header>
  <a class="brand abs" href="http://harborlinecoveragepartners.example/">
    <span class="brand-square"></span>
    <span class="brand-name">Harborline Coverage Partners</span>
  </a>
  <nav class="main-nav abs">
    <a class="current" href="#">Home</a>
    <a href="#">About Us</a>
    <a href="#">Solutions for Diverse Needs</a>
    <a href="#">Case Studies</a>
  </nav>
</header>

<svg class="hero abs" width="1016" height="360" viewBox="0 78 1016 360" role="img" aria-label="Four overlapping circular photos of international families and advisers outdoors">
  <defs>
    <linearGradient id="g1" x1="0" y1="0" x2="0" y2="1"><stop offset="0" stop-color="#c9d4dc"/><stop offset=".5" stop-color="#c59a82"/><stop offset="1" stop-color="#e7d7b8"/></linearGradient>
    <linearGradient id="g2" x1="0" y1="0" x2="0" y2="1"><stop offset="0" stop-color="#d9c7ae"/><stop offset=".45" stop-color="#6b7fa6"/><stop offset="1" stop-color="#c7a983"/></linearGradient>
    <linearGradient id="g3" x1="0" y1="0" x2="0" y2="1"><stop offset="0" stop-color="#b9c8d4"/><stop offset=".5" stop-color="#4a4a4c"/><stop offset="1" stop-color="#d7c8b2"/></linearGradient>
    <linearGradient id="g4" x1="0" y1="0" x2="0" y2="1"><stop offset="0" stop-color="#2f6fc2"/><stop offset=".55" stop-color="#8bb7e3"/><stop offset="1" stop-color="#6f9a3a"/></linearGradient>
  </defs>
  <circle cx="209" cy="258" r="178" fill="url(#g1)" stroke="#aaa"/>
  <circle cx="806" cy="258" r="178" fill="url(#g4)" stroke="#aaa"/>
  <circle cx="635" cy="258" r="178" fill="url(#g3)" stroke="#aaa"/>
  <circle cx="428" cy="258" r="178" fill="url(#g2)" stroke="#aaa"/>
</svg>
<div class="slider-dots abs"><span class="active"></span><span></span><span></span><span></span></div>

<aside>
  <article class="service-card card-banking abs" style="top:463px">
    <div class="photo" role="img" aria-label="Advisers reviewing a wealth plan at a private bank"></div>
    <h2>Private Banking</h2>
    <p>Coverage solutions that private banks integrate into wealth preservation strategies for their ultra high net worth clients.</p>
    <span class="more">Read More..</span>
  </article>
  <article class="service-card card-estate abs" style="top:683px">
    <div class="photo" role="img" aria-label="Documents and a pen on an adviser's desk"></div>
    <h2>Estate Planning</h2>
    <p>Cross-border estate and tax planning support for families whose assets span several countries and jurisdictions.</p>
    <span class="more">Read More..</span>
  </article>
  <article class="service-card card-life abs" style="top:904px">
    <div class="photo" role="img" aria-label="Family on a beach under a blue sky"></div>
    <h2>Life Insurance</h2>
    <p>From simple life policies to complex, sophisticated cases placed with leading international carriers worldwide.</p>
    <span class="more">Read More..</span>
  </article>
</aside>

<main>
  <h1 class="about-title abs">A Few Words About Us</h1>
  <div class="about-photo abs" role="img" aria-label="Close-up of a young hand holding an elderly hand"></div>
  <p class="about-copy lead abs">We are a boutique financial services firm serving private banks and financial institutions whose clients hold ultra high net worth across borders. Our specialists design solutions that financial professionals can integrate into comprehensive wealth preservation strategies. The work may run the spectrum from simple life insurance products to complex cases with sophisticated and intricate structures, drawing on deep expertise in international taxation, estate planning and business insurance, and on long relationships with leading carriers in every major market.</p>
  <p class="about-copy rest abs">Our audience is the financial services professional, not the end client. We work discreetly alongside private bankers, trustees and family offices, giving them unparalleled expertise in wealth preservation, taxation and business insurance so they can serve international families with confidence across generations and jurisdictions.</p>
  <a class="read-more abs" href="#" style="right:32px;top:792px">Read More..</a>

  <section class="login abs">
    <div class="login-inner">
      <h3>Customer Login</h3>
      <p class="intro">Pay your bills, report or track a claim, manage your policy.</p>
      <a class="register" href="#">Learn More or Register Now</a>
      <label class="field">User Name : <input type="text"></label>
      <span class="forgot">Forget Username?</span>
      <label class="field">Password : <input type="password"></label>
      <span class="forgot">Forget Password?</span>
      <button type="button">Login</button>
    </div>
  </section>

  <h2 class="advantages-title abs">Our Advantages</h2>
  <ul class="advantage-list abs" style="left:610px">
    <li>Global Reach</li><li>Tax Expertise</li><li>Estate Plans</li><li>Private Banks</li><li>Top Carriers</li><li>Discretion</li><li>Family Offices</li><li>Trust Support</li><li>Case Design</li>
  </ul>
  <ul class="advantage-list abs" style="left:818px">
    <li>Key Person</li><li>Buy-Sell Plans</li><li>Premium Finance</li><li>Multi-Currency</li><li>Underwriting</li><li>Fast Placement</li><li>Policy Review</li><li>Legacy Plans</li><li>Adviser Tools</li>
  </ul>
  <a class="read-more abs" href="#" style="right:32px;top:1102px">Read More..</a>
</main>

<footer class="site-footer abs">
  <span class="copy">Copyright 2012.All rights reserved.</span>
  <div class="follow">
    <span class="label">Follow Us :</span>
    <a href="#" aria-label="Share">
      <svg width="18" height="18" viewBox="0 0 18 18" fill="#333"><circle cx="4" cy="9" r="2.6"/><circle cx="14" cy="4" r="2.6"/><circle cx="14" cy="14" r="2.6"/><path d="M4 9L14 4M4 9L14 14" stroke="#333" stroke-width="1.6"/></svg>
    </a>
    <a href="#" aria-label="Messages">
      <svg width="18" height="18" viewBox="0 0 18 18" fill="#333"><path d="M2 3h14v9H7l-4 3v-3H2z"/></svg>
    </a>
    <a href="#" aria-label="Email updates">
      <svg width="18" height="18" viewBox="0 0 18 18" fill="none" stroke="#333" stroke-width="1.8"><rect x="2" y="4" width="14" height="10"/><path d="M2 4l7 6 7-6"/></svg>
    </a>
  </div>
</footer>

</body>
</html>
```